Re-style home page - eye-catching and unique design for social commerce website

We need a new concept design for Trondix's home page.
We don't want to make huge changes but creating a more professional and eye-catching style.

We need to look very serious like a professional services company and in the same time to look like a social network for e-commerce.

Our logo is very captive and you can use to creating something of harmonious.

This is a re-style and I'm excepted to see unique and fresh design like Glimmora.
Updates

Target Market(s)

e-commerce and social

Industry/Entity Type

Social

Number of Pages Required

1 page

Font styles to use
Serif
Sans Serif

Requirements
Must have
• An eye-catching result.
• Search bar with logo and Login How it works and business
• The slogan with login and signup.
• Footer links.
Nice to have
• I would like to open the home page and see only two clear ways:
• -Consumer
• --Search
• --The slogan
• --Login and Signup
• --How it works
• -Business
• --Go to Business area
• Background: City, Shopping.
Should not have
• Scrollbar style!

```html
<!DOCTYPE html>
<html lang="en">
<head>
<meta charset="utf-8">
<title>Trondix — Shop directly from your profile</title>
<link href="https://fonts.googleapis.com/css2?family=Montserrat:wght@400;500;600;700&family=Open+Sans:wght@300;400&display=swap" rel="stylesheet">
<style>
  :root {
    --city-top: #5a5673;
    --city-mid: #3c3a5c;
    --city-bottom: #262652;
    --header-bg: rgba(28, 28, 62, 0.72);
    --white: #ffffff;
    --field-bg: #ffffff;
    --field-text: #444650;
    --chevron: #b9bcc4;
    --signup: #d8302f;
    --cta: #7ab72f;
    --search-bg: rgba(255, 255, 255, 0.82);
    --search-text: #7c8088;
    --hero-a: #6f9c9a;
    --hero-b: #8fb2ae;
    --hero-c: #b99a93;
    --avatar-ring: #ffffff;
    --avatar-fill: #c99a84;
    --dots: rgba(220, 222, 235, 0.7);
  }
  * { box-sizing: border-box; margin: 0; padding: 0; }
  html, body { width: 1200px; height: 675px; overflow: hidden; }
  body { font-family: "Montserrat", sans-serif; color: var(--white); }

  .page {
    position: relative; width: 1200px; height: 675px; overflow: hidden;
  }
  .city-backdrop {
    position: absolute; inset: 0;
    background:
      radial-gradient(ellipse at 30% 30%, rgba(140, 130, 150, 0.45), transparent 55%),
      radial-gradient(ellipse at 80% 25%, rgba(170, 160, 180, 0.35), transparent 50%),
      linear-gradient(180deg, var(--city-top) 0%, var(--city-mid) 50%, var(--city-bottom) 100%);
  }

  .site-header {
    position: absolute; left: 0; top: 0; width: 1200px; height: 59px;
    background: var(--header-bg);
  }
  .brand {
    position: absolute; left: 26px; top: 13px;
    font-weight: 700; font-size: 27px; line-height: 32px; color: var(--white);
    letter-spacing: 0.5px;
  }
  .feed-label {
    position: absolute; left: 295px; top: 22px;
    font-size: 11px; font-weight: 600; line-height: 14px;
  }
  .select {
    position: absolute; top: 12px; width: 176px; height: 33px;
    background: var(--field-bg); border-radius: 3px;
    color: var(--field-text); font-family: "Open Sans", sans-serif; font-size: 12px;
    display: flex; align-items: center; padding: 0 12px;
  }
  .select .chevron { position: absolute; right: 10px; top: 12px; }
  .select--interest { left: 399px; }
  .select--city { left: 584px; padding-left: 28px; }
  .select--city .pin { position: absolute; left: 11px; top: 9px; }
  .btn-signup {
    position: absolute; left: 773px; top: 12px; width: 84px; height: 35px;
    background: var(--signup); border-radius: 3px;
    font-size: 13px; font-weight: 500; display: flex; align-items: center; justify-content: center;
  }
  .link-login {
    position: absolute; left: 871px; top: 20px; font-size: 13px; font-weight: 500;
  }

  .network { position: absolute; inset: 0; }

  .hero-card {
    position: absolute; left: 350px; top: 194px; width: 500px; height: 252px;
    border-radius: 3px; overflow: hidden;
  }
  .hero-photo {
    position: absolute; inset: 0;
    background:
      radial-gradient(ellipse at 80% 55%, rgba(200, 150, 140, 0.6), transparent 45%),
      linear-gradient(100deg, var(--hero-a) 0%, var(--hero-b) 55%, var(--hero-c) 100%);
  }
  .hero-title {
    position: absolute; left: 0; right: 0; top: 238px;
    text-align: center; font-family: "Open Sans", sans-serif; font-weight: 300;
    font-size: 33px; line-height: 42px;
  }
  .search {
    position: absolute; left: 437px; top: 298px; width: 325px; height: 41px;
    background: var(--search-bg); border-radius: 2px;
    font-family: "Open Sans", sans-serif; font-size: 13px; color: var(--search-text);
    display: flex; align-items: center; padding-left: 17px;
  }
  .search-icon { position: absolute; left: 777px; top: 311px; }
  .btn-business {
    position: absolute; left: 510px; top: 361px; width: 180px; height: 34px;
    background: var(--cta); border-radius: 2px;
    font-size: 12px; font-weight: 500; display: flex; align-items: center; justify-content: center; gap: 6px;
  }
  .link-how {
    position: absolute; left: 0; right: 0; top: 407px; text-align: center;
    font-family: "Open Sans", sans-serif; font-size: 12px;
  }

  .site-footer .footer-links {
    position: absolute; left: 0; right: 0; top: 575px;
    display: flex; justify-content: center; gap: 26px;
    font-size: 10.5px; font-weight: 500; list-style: none;
  }
  .copyright {
    position: absolute; left: 0; right: 0; top: 603px; text-align: center;
    font-size: 9.5px; font-weight: 500;
  }
</style>
</head>
<body>
<div class="page">
  <div class="city-backdrop" role="img" aria-label="Blurred photograph of a busy city shopping street with crowds of shoppers"></div>

  <header class="site-header">
    <div class="brand">Trondix</div>
    <span class="feed-label">Setup your feed</span>
    <div class="select select--interest">Active life
      <svg class="chevron" width="13" height="8" viewBox="0 0 13 8"><path d="M1 1l5.5 5.5L12 1" fill="none" stroke="var(--chevron)" stroke-width="1.4"/></svg>
    </div>
    <div class="select select--city">
      <svg class="pin" width="11" height="15" viewBox="0 0 11 15"><path d="M5.5 0.5a5 5 0 0 0-5 5c0 3.7 5 9 5 9s5-5.3 5-9a5 5 0 0 0-5-5z" fill="var(--chevron)"/><circle cx="5.5" cy="5.5" r="1.8" fill="#fff"/></svg>
      London
      <svg class="chevron" width="13" height="8" viewBox="0 0 13 8"><path d="M1 1l5.5 5.5L12 1" fill="none" stroke="var(--chevron)" stroke-width="1.4"/></svg>
    </div>
    <div class="btn-signup">Sign Up</div>
    <div class="link-login">Login</div>
  </header>

  <svg class="network" width="1200" height="675" viewBox="0 0 1200 675">
    <g fill="none" stroke="var(--dots)" stroke-width="1.6" stroke-dasharray="2 3" stroke-linecap="round">
      <path d="M306 183 Q318 205 350 210"/>
      <path d="M365 156 Q372 180 380 194"/>
      <path d="M413 178 Q405 188 405 194"/>
      <path d="M470 173 Q466 186 460 194"/>
      <path d="M700 183 Q706 190 712 194"/>
      <path d="M760 156 Q770 178 778 194"/>
      <path d="M806 178 Q802 188 800 194"/>
      <path d="M864 172 Q856 190 846 200"/>
      <path d="M312 368 Q325 382 350 386"/>
      <path d="M283 450 Q300 410 350 402"/>
      <path d="M356 482 Q378 470 386 446"/>
      <path d="M893 393 Q880 416 850 418"/>
      <path d="M908 440 Q880 452 805 446"/>
      <path d="M840 476 Q822 462 808 446"/>
      <path d="M768 490 Q720 480 712 446"/>
    </g>
    <g fill="var(--avatar-fill)" stroke="var(--avatar-ring)" stroke-width="2.5">
      <circle cx="300" cy="167" r="14" role="img" aria-label="Member portrait"/>
      <circle cx="361" cy="140" r="14" role="img" aria-label="Member portrait"/>
      <circle cx="415" cy="162" r="14" role="img" aria-label="Member portrait"/>
      <circle cx="474" cy="157" r="14" role="img" aria-label="Member portrait"/>
      <circle cx="695" cy="167" r="14" role="img" aria-label="Member portrait"/>
      <circle cx="756" cy="140" r="14" role="img" aria-label="Member portrait"/>
      <circle cx="809" cy="162" r="14" role="img" aria-label="Member portrait"/>
      <circle cx="870" cy="157" r="14" role="img" aria-label="Member portrait"/>
      <circle cx="303" cy="354" r="14" role="img" aria-label="Member portrait"/>
      <circle cx="275" cy="464" r="14" role="img" aria-label="Member portrait"/>
      <circle cx="348" cy="496" r="14" role="img" aria-label="Member portrait"/>
      <circle cx="896" cy="377" r="14" role="img" aria-label="Member portrait"/>
      <circle cx="922" cy="437" r="14" role="img" aria-label="Member portrait"/>
      <circle cx="852" cy="486" r="14" role="img" aria-label="Member portrait"/>
      <circle cx="778" cy="502" r="14" role="img" aria-label="Member portrait"/>
    </g>
  </svg>

  <section class="hero-card">
    <div class="hero-photo" role="img" aria-label="Close-up photograph of a young woman in large round sunglasses"></div>
  </section>
  <h1 class="hero-title">Shop directly from your profile</h1>
  <div class="search">Search keyword</div>
  <svg class="search-icon" width="20" height="20" viewBox="0 0 20 20"><circle cx="8" cy="8" r="6" fill="none" stroke="#fff" stroke-width="2.6"/><path d="M12.5 12.5l5.5 5.5" stroke="#fff" stroke-width="3" stroke-linecap="round"/></svg>
  <div class="btn-business">Go to Business Area
    <svg width="18" height="8" viewBox="0 0 18 8"><path d="M0 4h16M13 1l3 3-3 3" fill="none" stroke="#fff" stroke-width="1"/></svg>
  </div>
  <div class="link-how">How it works</div>

  <footer class="site-footer">
    <ul class="footer-links">
      <li>About Us</li><li>Blog</li><li>Business</li><li>Jobs</li><li>Privacy</li><li>FAQ</li><li>Contacts</li>
    </ul>
    <p class="copyright">© 2015 Trondix. All right reserved.</p>
  </footer>
</div>
</body>
</html>
```